Harold Brisk Mechanical business cards

We need business cards designed for "Harold Brisk Mechanical" "Mechanical & Electrical Contractors" "Specializing in Service & Installation"
"Cooling, Heating, Service, Installations, Residential, Commercial"

```html
<!DOCTYPE html>
<html lang="en">
<head>
<meta charset="utf-8">
<title>Harold Brisk Mechanical – Business Cards</title>
<link href="https://fonts.googleapis.com/css2?family=Lato:ital,wght@0,400;0,700;0,900;1,400&display=swap" rel="stylesheet">
<style>
  :root {
    --bg: #2b2b2d;
    --card-black: #121213;
    --card-white: #ffffff;
    --brand-red: #e0001f;
    --ink: #161616;
    --soft-white: #e9e9e9;
    --grey-text: #bdbdbd;
  }
  * { box-sizing: border-box; margin: 0; padding: 0; }
  html, body { width: 1200px; height: 716px; overflow: hidden; }
  body {
    background: var(--bg);
    font-family: "Lato", sans-serif;
    position: relative;
  }
  .card {
    position: absolute;
    top: 203px;
    width: 540px;
    height: 310px;
    border-radius: 18px;
    overflow: hidden;
  }
  /* Back of card */
  .card-back { left: 40px; background: var(--card-black); }
  .card-back .tagline {
    position: absolute; left: 34px; top: 32px;
    color: var(--brand-red); font-size: 15px; font-style: italic;
  }
  .services { list-style: none; position: absolute; left: 34px; top: 66px; }
  .services li {
    display: flex; align-items: center; gap: 6px;
    color: var(--soft-white); font-size: 15px; line-height: 27px;
  }
  .services svg { width: 14px; height: 14px; }
  .wordmark {
    position: absolute; display: flex; align-items: center; gap: 10px;
  }
  .wordmark .mark-square { width: 30px; height: 30px; background: var(--brand-red); flex: none; }
  .wordmark .mark-name {
    font-weight: 900; font-size: 20px; line-height: 22px; letter-spacing: 0.5px; text-transform: uppercase;
  }
  .card-back .wordmark { right: 34px; bottom: 38px; }
  .card-back .mark-name { color: var(--soft-white); }

  /* Front of card */
  .card-front { left: 620px; background: var(--card-white); }
  .card-front .shapes { position: absolute; inset: 0; }
  .person { position: absolute; left: 34px; top: 30px; }
  .person .name { font-weight: 900; font-size: 21px; color: var(--ink); letter-spacing: 0.5px; }
  .person .role { font-size: 13px; color: var(--brand-red); letter-spacing: 0.5px; margin-top: 2px; }
  .person .rule { width: 56px; height: 3px; background: var(--brand-red); margin-top: 5px; }
  .contact { position: absolute; left: 26px; list-style: none; }
  .contact li {
    display: flex; align-items: center; gap: 10px;
    color: var(--card-white); font-size: 15px; line-height: 24px;
  }
  .contact .icon {
    width: 18px; height: 18px; border-radius: 4px; background: var(--brand-red);
    display: flex; align-items: center; justify-content: center; flex: none;
  }
  .contact .icon svg { width: 12px; height: 12px; }
  .contact-phone { top: 128px; left: 46px !important; }
  .contact-web { top: 184px; }
  .card-front .wordmark { right: 30px; top: 150px; }
  .card-front .mark-name { color: var(--ink); }
  .social { position: absolute; right: 40px; top: 246px; display: flex; gap: 14px; }
  .social span { width: 18px; height: 18px; border-radius: 3px; background: var(--ink); }
</style>
</head>
<body>

<section class="card card-back" aria-label="Card back">
  <p class="tagline">Specializing in Service &amp; Installation</p>
  <ul class="services">
    <li><svg viewBox="0 0 14 14"><path d="M2 7l3 3 7-8" fill="none" stroke="#e0001f" stroke-width="2.4"/></svg>Cooling</li>
    <li><svg viewBox="0 0 14 14"><path d="M2 7l3 3 7-8" fill="none" stroke="#e0001f" stroke-width="2.4"/></svg>Heating</li>
    <li><svg viewBox="0 0 14 14"><path d="M2 7l3 3 7-8" fill="none" stroke="#e0001f" stroke-width="2.4"/></svg>Service</li>
    <li><svg viewBox="0 0 14 14"><path d="M2 7l3 3 7-8" fill="none" stroke="#e0001f" stroke-width="2.4"/></svg>Installations</li>
    <li><svg viewBox="0 0 14 14"><path d="M2 7l3 3 7-8" fill="none" stroke="#e0001f" stroke-width="2.4"/></svg>Residential</li>
    <li><svg viewBox="0 0 14 14"><path d="M2 7l3 3 7-8" fill="none" stroke="#e0001f" stroke-width="2.4"/></svg>Commercial</li>
  </ul>
  <div class="wordmark">
    <span class="mark-square"></span>
    <span class="mark-name">Harold Brisk<br>Mechanical</span>
  </div>
</section>

<section class="card card-front" aria-label="Card front">
  <svg class="shapes" viewBox="0 0 540 310" width="540" height="310" aria-hidden="true">
    <path d="M0 112 H322 L336 126 V236 H0 Z" fill="#161616"/>
    <line x1="0" y1="176" x2="336" y2="176" stroke="#ffffff" stroke-width="2"/>
    <path d="M0 236 H344 L368 212 H540 V284 H0 Z" fill="#e0001f"/>
  </svg>

  <div class="person">
    <p class="name">HAROLD BRISK</p>
    <p class="role">JOB TITLE</p>
    <div class="rule"></div>
  </div>

  <ul class="contact contact-phone">
    <li><span class="icon"><svg viewBox="0 0 12 12"><path d="M2 1h3l1 3-2 1a7 7 0 0 0 3 3l1-2 3 1v3c-6 0-9-3-9-9z" fill="#fff"/></svg></span>000 000 0000</li>
    <li><span class="icon"><svg viewBox="0 0 12 12"><rect x="3" y="1" width="6" height="10" rx="1" fill="none" stroke="#fff" stroke-width="1.4"/></svg></span>000 000 0000</li>
  </ul>
  <ul class="contact contact-web">
    <li><span class="icon"><svg viewBox="0 0 12 12"><rect x="1" y="3" width="10" height="7" fill="none" stroke="#fff" stroke-width="1.3"/><path d="M1 3l5 4 5-4" fill="none" stroke="#fff" stroke-width="1.3"/></svg></span>youremail@yxz.com</li>
    <li><span class="icon"><svg viewBox="0 0 12 12"><circle cx="6" cy="6" r="4.6" fill="none" stroke="#fff" stroke-width="1.3"/><path d="M1.4 6h9.2M6 1.4c-2 2.5-2 6.7 0 9.2M6 1.4c2 2.5 2 6.7 0 9.2" fill="none" stroke="#fff" stroke-width="1"/></svg></span>www.yourwebsite.com</li>
  </ul>

  <div class="wordmark">
    <span class="mark-square"></span>
    <span class="mark-name">Harold Brisk<br>Mechanical</span>
  </div>

  <div class="social" aria-label="Social links">
    <span></span><span></span><span></span><span></span>
  </div>
</section>

</body>
</html>
```